Landing Page Only for text marketing service msgzeta.net

Our current site msgzeta.net needs a custom landing page for paid advertisements that is conversion centered as well as clear and concise. We want to focus on displaying the information effectively without getting too wordy or confusing to gain a higher conversion rate as our main goal.

We want more emphasis on the Try for $1 that includes 500 messages and custom keyword. The offer has no commitments. Upgrade or cancel at anytime.

We also want the landing page to focus on the benefits and marketing advantages (found in benefits tab), possible uses: mobile coupons, reminders/alerts, contests, daily specials, etc. (more examples can be found in how it works tab), and how it works.

The landing page can link to other parts of the site or use any information from other parts of the site. Our logo is attached in files. We want the design to match the overall color scheme of the site.

Target Market(s)

US based customers, business owners.

Industry/Entity Type

Marketing

Coding

Coded - Design and coding required

Number of Pages Required

1 page

Requirements
Must have
• See project description.
Nice to have
• See project description and any additional ideas welcomed from the designer.

```html
<!DOCTYPE html>
<html lang="en">
<head>
<meta charset="utf-8">
<title>MsgZeta – Try SMS Marketing for $1</title>
<link rel="stylesheet" href="https://fonts.googleapis.com/css2?family=Raleway:wght@400;500;600;700;800&family=Open+Sans:wght@400;600&family=Noto+Serif:wght@400&display=swap">
<style>
:root{
  --red:#c8202a;
  --red-dark:#a8161f;
  --ink:#333;
  --body:#555;
  --muted:#888;
  --dark:#3d3d3d;
  --darker:#333;
  --footer:#3a3a3a;
  --footer-bar:#2e2e2e;
  --light:#fff;
  --line:#d9d9d9;
}
*{margin:0;padding:0;box-sizing:border-box}
html,body{width:1200px;height:3197px;overflow:hidden;background:#fff}
body{font-family:"Open Sans",Arial,sans-serif;color:var(--body);position:relative}
.abs{position:absolute}
h2,h3,h4{font-family:"Raleway",Arial,sans-serif}

/* header */
.site-header{position:absolute;top:0;left:0;width:1200px;height:115px;border-top:4px solid var(--red);background:#fff;box-shadow:0 2px 6px rgba(0,0,0,.06);z-index:2}
.brand{position:absolute;left:130px;top:22px;display:flex;align-items:center;gap:10px}
.brand-mark{width:22px;height:22px;border-radius:50%;background:var(--red)}
.brand-name{font-family:"Raleway",sans-serif;font-weight:600;font-size:38px;color:#555;letter-spacing:1px}
.header-contact{position:absolute;right:235px;top:30px;font-family:"Raleway",sans-serif;font-size:13px;color:#555;display:flex;align-items:center;gap:10px;letter-spacing:.3px}
.header-contact svg{width:12px;height:12px}
.login-btn{position:absolute;left:980px;top:24px;width:86px;height:30px;background:var(--red);color:#fff;font-family:"Raleway",sans-serif;font-weight:600;font-size:12px;border-radius:3px;display:flex;align-items:center;justify-content:center;gap:6px}
.main-nav{position:absolute;right:134px;top:74px;display:flex;gap:38px;font-family:"Raleway",sans-serif;font-weight:600;font-size:12.5px;letter-spacing:.8px;color:#555}
.main-nav .active{color:var(--red)}

/* hero */
.hero{position:absolute;top:115px;left:0;width:1200px;height:485px;background:linear-gradient(90deg,#f4f4f2 0%,#eeeeec 40%,#d8d6cf 60%,#8d8a6a 100%)}
.hero-photo{position:absolute;right:0;top:0;width:640px;height:485px;background:radial-gradient(ellipse at 55% 40%,#e6c7b0 0%,#b89478 30%,#7b7a55 65%,#5e6046 100%);opacity:.9;-webkit-mask-image:linear-gradient(90deg,transparent 0,#000 30%);mask-image:linear-gradient(90deg,transparent 0,#000 30%)}
.hero-eyebrow{position:absolute;left:132px;top:70px;font-family:"Noto Serif",serif;font-size:20px;letter-spacing:2.5px;line-height:33px;color:#333}
.hero-title{position:absolute;left:132px;top:135px;font-family:"Raleway",sans-serif;font-weight:800;font-size:46px;letter-spacing:2.5px;color:var(--red)}
.hero-list{position:absolute;left:132px;top:205px;list-style:none;font-family:"Noto Serif",serif;font-size:16.5px;color:#333}
.hero-list li{display:flex;align-items:center;gap:14px;height:32px}
.hero-list li:last-child{margin-top:3px}
.hero-list svg{width:22px;height:18px}
.btn-red{position:absolute;left:132px;top:360px;width:170px;height:50px;background:var(--red);color:#fff;font-family:"Raleway",sans-serif;font-weight:700;font-size:17px;border-radius:3px;display:flex;align-items:center;justify-content:center;letter-spacing:.5px}

/* sections */
.section-title{position:absolute;left:0;width:1200px;text-align:center;font-weight:700;letter-spacing:3px}
.section-sub{position:absolute;left:0;width:1200px;text-align:center;font-size:16px;letter-spacing:.8px}

.benefits{position:absolute;top:600px;left:0;width:1200px;height:395px}
.benefits .section-title{top:37px;font-size:29px;color:var(--red)}
.benefits .section-sub{top:82px;color:#555}
.benefit{position:absolute;top:130px;width:260px;text-align:center}
.benefit svg{width:130px;height:140px}
.benefit p{font-family:"Raleway",sans-serif;font-size:19px;color:#333;margin-top:30px}
.benefit.highlight p{color:var(--red)}

.advantages{position:absolute;top:995px;left:0;width:1200px;height:613px;background:var(--dark);color:#fff}
.advantages .section-title{top:48px;font-size:29px}
.advantages .section-sub{top:100px;font-size:14.5px;color:#999}
.adv{position:absolute;width:300px;text-align:center}
.adv svg{width:34px;height:34px}
.adv h3{font-size:19px;font-weight:700;letter-spacing:1.8px;margin-top:18px}
.adv p{font-size:12.5px;line-height:21px;color:#ddd;margin-top:14px;letter-spacing:.4px}

.support{position:absolute;top:1608px;left:0;width:1200px;height:250px;background:linear-gradient(180deg,#d5232c 0%,#b0171f 100%);color:#fff}
.support .section-title{top:30px;font-size:29px}
.support-text{position:absolute;left:220px;width:760px;top:88px;text-align:center;font-size:12.5px;line-height:22px;letter-spacing:.4px}
.btn-dark{position:absolute;left:512px;top:158px;width:176px;height:46px;background:#333;border-radius:23px;color:#fff;font-family:"Raleway",sans-serif;font-weight:700;font-size:17px;display:flex;align-items:center;justify-content:center}

.why{position:absolute;top:1858px;left:0;width:1200px;height:450px}
.why .section-title{top:44px;font-size:29px;color:var(--red)}
.why .section-sub{top:95px;color:#555}
.why-item{position:absolute;width:290px;padding-left:63px}
.why-item svg{position:absolute;left:0;top:0;width:40px;height:40px}
.why-item h4{font-size:19px;font-weight:500;color:#333;letter-spacing:.3px}
.why-item.highlight h4{color:var(--red)}
.why-item p{font-size:11.5px;line-height:23px;margin-top:10px;color:#444;text-align:justify}

.testimonial{position:absolute;top:2308px;left:0;width:1200px;height:275px;background:linear-gradient(100deg,#4a4440 0%,#2e2c2c 40%,#242628 70%,#3c3e44 100%)}
.avatar{position:absolute;left:548px;top:20px;width:104px;height:104px;border-radius:50%;background:#bcbcbc;border:4px solid #fff}
.quote{position:absolute;left:0;width:1200px;top:150px;text-align:center;color:#eee;font-size:14px;line-height:24px;letter-spacing:.4px}
.quote-author{position:absolute;left:0;width:1200px;top:205px;text-align:center;color:var(--red);font-size:13px}
.dots{position:absolute;left:588px;top:238px;display:flex;gap:8px}
.dots i{width:5px;height:5px;border-radius:50%;background:#777}
.dots i:first-child{background:#ccc}

.clients{position:absolute;top:2583px;left:0;width:1200px;height:287px}
.clients .section-title{top:48px;font-size:29px;color:var(--red)}
.client{position:absolute;top:117px;width:216px;height:120px;border:4px solid var(--line);display:flex;align-items:center;justify-content:center;gap:10px;font-family:"Raleway",sans-serif;font-weight:700;font-size:26px;color:#555}
.client i{width:16px;height:16px;background:var(--red)}

.site-footer{position:absolute;top:2870px;left:0;width:1200px;height:260px;background:var(--footer);border-top:5px solid var(--red);color:#fff}
.footer-col{position:absolute;top:45px}
.footer-col h4{font-size:18px;font-weight:700;letter-spacing:1.5px;margin-bottom:14px}
.footer-col li{list-style:none;font-size:11.5px;color:#999;line-height:22px}
.footer-brand{position:absolute;left:835px;top:70px;display:flex;align-items:center;gap:12px;opacity:.35}
.footer-brand .brand-mark{background:#aaa}
.footer-brand .brand-name{color:#aaa;font-size:42px}
.footer-bar{position:absolute;top:3130px;left:0;width:1200px;height:67px;background:var(--footer-bar);color:#888;font-size:11px}
.footer-bar .copy{position:absolute;left:132px;top:26px}
.social{position:absolute;left:950px;top:20px;display:flex;gap:12px}
.social i{width:30px;height:30px;border-radius:50%;background:#6a6a6a}
</style>
</head>
<body>

<header class="site-header">
  <div class="brand"><span class="brand-mark"></span><span class="brand-name">MsgZeta</span></div>
  <div class="header-contact">QUESTIONS? CONTACT THE TEAM
    <svg viewBox="0 0 12 12"><path d="M2 1l2 0 1 3-1.5 1a6 6 0 0 0 3.5 3.5L8 7l3 1v2a1 1 0 0 1-1 1A9 9 0 0 1 1 2a1 1 0 0 1 1-1z" fill="#888"/></svg>
    1-800-555-0142</div>
  <div class="login-btn"><svg width="9" height="11" viewBox="0 0 9 11"><rect x="1" y="5" width="7" height="5.5" fill="none" stroke="#fff"/><path d="M2.5 5V3.3a2 2 0 0 1 4 0V5" fill="none" stroke="#fff"/></svg>LOGIN</div>
  <nav class="main-nav"><span class="active">HOME</span><span>PRICING</span><span>BENEFITS</span><span>HOW IT WORKS</span><span>RESELLERS</span><span>SIGN UP</span></nav>
</header>

<section class="hero">
  <div class="hero-photo" role="img" aria-label="Photo of a smiling woman reading a text message on her phone"></div>
  <p class="hero-eyebrow">THE MOST COST-EFFECTIVE<br>SMS MESSAGING</p>
  <h1 class="hero-title">TRY FOR $1</h1>
  <ul class="hero-list">
    <li><svg viewBox="0 0 22 18"><path d="M2 9l6 6L20 2" fill="none" stroke="#6ab23a" stroke-width="4"/></svg>500 messages</li>
    <li><svg viewBox="0 0 22 18"><path d="M2 9l6 6L20 2" fill="none" stroke="#6ab23a" stroke-width="4"/></svg>custom keyword</li>
    <li><svg viewBox="0 0 22 18"><path d="M2 9l6 6L20 2" fill="none" stroke="#6ab23a" stroke-width="4"/></svg>The offer has no commitments</li>
    <li><svg viewBox="0 0 22 18"><path d="M2 9l6 6L20 2" fill="none" stroke="#6ab23a" stroke-width="4"/></svg>Upgrade or cancel at anytime</li>
  </ul>
  <a class="btn-red">GET STARTED</a>
</section>

<section class="benefits">
  <h2 class="section-title">OUR BENEFITS</h2>
  <p class="section-sub">Did you know over 83% of texts are read within an hour?</p>
  <div class="benefit highlight" style="left:240px">
    <svg viewBox="0 0 130 140"><path d="M66 26A55 55 0 1 0 110 60" fill="none" stroke="#c8202a" stroke-width="5"/><path d="M84 10l26 16-26 16z" fill="none" stroke="#c8202a" stroke-width="5" stroke-linejoin="round"/><rect x="40" y="68" width="36" height="22" fill="none" stroke="#333" stroke-width="3"/><circle cx="58" cy="79" r="6" fill="none" stroke="#333" stroke-width="3"/><path d="M46 94h36V72" fill="none" stroke="#333" stroke-width="3"/></svg>
    <p>INCREASE REVENUE</p>
  </div>
  <div class="benefit" style="left:475px">
    <svg viewBox="0 0 130 140"><path d="M66 26A55 55 0 1 0 110 60" fill="none" stroke="#333" stroke-width="5"/><path d="M84 10l26 16-26 16z" fill="none" stroke="#333" stroke-width="5" stroke-linejoin="round"/><path d="M44 72l20-16 20 16v24H44z" fill="none" stroke="#333" stroke-width="3"/><path d="M44 72l20 14 20-14" fill="none" stroke="#333" stroke-width="3"/><path d="M54 64h20M54 70h20" stroke="#333" stroke-width="2"/></svg>
    <p>LIFT YOUR WORKLOAD</p>
  </div>
  <div class="benefit" style="left:710px">
    <svg viewBox="0 0 130 140"><path d="M66 26A55 55 0 1 0 110 60" fill="none" stroke="#333" stroke-width="5"/><path d="M84 10l26 16-26 16z" fill="none" stroke="#333" stroke-width="5" stroke-linejoin="round"/><path d="M46 62l32 32M78 62L46 94" stroke="#333" stroke-width="4" stroke-linecap="round"/><circle cx="46" cy="62" r="6" fill="none" stroke="#333" stroke-width="3"/><circle cx="80" cy="94" r="5" fill="none" stroke="#333" stroke-width="3"/></svg>
    <p>WEBINARS</p>
  </div>
</section>

<section class="advantages">
  <h2 class="section-title">MARKETING ADVANTAGES</h2>
  <p class="section-sub">We support all the major wireless carriers to effectively market your clientele.</p>
  <div class="adv" style="left:120px;top:180px"><svg viewBox="0 0 34 34"><rect x="2" y="7" width="30" height="20" rx="2" fill="none" stroke="#fff" stroke-width="1.6"/><path d="M2 13h30M6 21h10" stroke="#fff" stroke-width="1.6"/></svg><h3>MOBILE COUPONS</h3><p>Our user-friendly control panel and sched-<br>uler allow you to glide through set-up of<br>messaging needs</p></div>
  <div class="adv" style="left:450px;top:180px"><svg viewBox="0 0 34 34"><circle cx="17" cy="19" r="11" fill="none" stroke="#fff" stroke-width="1.6"/><path d="M17 12v7l5 3M5 8l5-4M29 8l-5-4" fill="none" stroke="#fff" stroke-width="1.6"/></svg><h3>ALERT CUSTOMERS</h3><p>Our user-friendly control panel and sched-<br>uler allow you to glide through set-up of<br>messaging needs</p></div>
  <div class="adv" style="left:780px;top:180px"><svg viewBox="0 0 34 34"><path d="M3 6h28v18H14l-6 5v-5H3z" fill="none" stroke="#fff" stroke-width="1.6"/><circle cx="11" cy="15" r="1.3" fill="#fff"/><circle cx="17" cy="15" r="1.3" fill="#fff"/><circle cx="23" cy="15" r="1.3" fill="#fff"/></svg><h3>CONTESTS</h3><p>Our user-friendly control panel and sched-<br>uler allow you to glide through set-up of<br>messaging needs</p></div>
  <div class="adv" style="left:120px;top:380px"><svg viewBox="0 0 34 34"><circle cx="17" cy="17" r="13" fill="none" stroke="#fff" stroke-width="1.6"/><path d="M17 9v9h-6" fill="none" stroke="#fff" stroke-width="1.6"/></svg><h3>DAILY SPECIALS</h3><p>Our user-friendly control panel and sched-<br>uler allow you to glide through set-up of<br>messaging needs</p></div>
  <div class="adv" style="left:450px;top:380px"><svg viewBox="0 0 34 34"><rect x="4" y="5" width="26" height="25" fill="none" stroke="#fff" stroke-width="1.6"/><path d="M4 11h26M10 2v6M24 2v6" stroke="#fff" stroke-width="1.6"/><text x="17" y="25" font-size="10" fill="#fff" text-anchor="middle" font-family="Open Sans">15</text></svg><h3>SCHEDULE MESSAGES</h3><p>Our user-friendly control panel and sched-<br>uler allow you to glide through set-up of<br>messaging needs</p></div>
  <div class="adv" style="left:780px;top:380px"><svg viewBox="0 0 34 34"><path d="M26 10A12 12 0 1 0 29 19" fill="none" stroke="#fff" stroke-width="1.6"/><path d="M21 4l6 6-7 3" fill="none" stroke="#fff" stroke-width="1.6"/></svg><h3>AUTO-RESPONDER</h3><p>Our user-friendly control panel and sched-<br>uler allow you to glide through set-up of<br>messaging needs</p></div>
</section>

<section class="support">
  <h2 class="section-title">100% LIVE SUPPORT!</h2>
  <p class="support-text">MsgZeta Support is all about making your life easier. Help is free forever, and you'll always get a real, live human to answer your questions or help you brainstorm ideas about how text marketing can work for you</p>
  <a class="btn-dark">TRY FOR $1</a>
</section>

<section class="why">
  <h2 class="section-title">WHY MSGZETA?</h2>
  <p class="section-sub">Start sending messages, adding subscribers and scheduling in minutes.</p>
  <div class="why-item highlight" style="left:132px;top:155px"><svg viewBox="0 0 40 40"><ellipse cx="20" cy="9" rx="14" ry="5" fill="none" stroke="#c8202a" stroke-width="2"/><path d="M6 9v20c0 3 6 5 14 5s14-2 14-5V9M6 16c0 3 6 5 14 5s14-2 14-5M6 23c0 3 6 5 14 5s14-2 14-5" fill="none" stroke="#c8202a" stroke-width="2"/></svg><h4>SAVE MONEY</h4><p>Our on-hand "Marketing Minds" are available via phone (Mon-Thurs 7AM-5PM &amp; Fri 7AM-3PM MST)</p></div>
  <div class="why-item" style="left:465px;top:155px"><svg viewBox="0 0 40 40"><path d="M4 14v22h32V14" fill="none" stroke="#333" stroke-width="2"/><path d="M20 28V4M12 12l8-8 8 8" fill="none" stroke="#333" stroke-width="2"/></svg><h4>DO IT FASTER</h4><p>Our on-hand "Marketing Minds" are available via phone (Mon-Thurs 7AM-5PM &amp; Fri 7AM-3PM MST)</p></div>
  <div class="why-item" style="left:790px;top:155px"><svg viewBox="0 0 40 40"><circle cx="20" cy="23" r="14" fill="none" stroke="#333" stroke-width="2"/><path d="M20 23V14M16 4h8M20 4v5" fill="none" stroke="#333" stroke-width="2"/></svg><h4>REMOVE FRUSTRATION</h4><p>Our on-hand "Marketing Minds" are available via phone (Mon-Thurs 7AM-5PM &amp; Fri 7AM-3PM MST)</p></div>
  <div class="why-item" style="left:132px;top:290px"><svg viewBox="0 0 40 40"><circle cx="20" cy="17" r="13" fill="none" stroke="#333" stroke-width="2"/><path d="M12 8c4 4 4 10 0 16M20 30v6M12 37h16" fill="none" stroke="#333" stroke-width="2"/></svg><h4>AMAZING SUPPORT</h4><p>Our on-hand "Marketing Minds" are available via phone (Mon-Thurs 7AM-5PM &amp; Fri 7AM-3PM MST)</p></div>
  <div class="why-item" style="left:465px;top:290px"><svg viewBox="0 0 40 40"><rect x="3" y="8" width="34" height="26" fill="none" stroke="#333" stroke-width="2"/><circle cx="13" cy="19" r="4" fill="none" stroke="#333" stroke-width="2"/><path d="M7 30c1-5 11-5 12 0M23 17h10M23 23h10M15 4h10v4H15z" fill="none" stroke="#333" stroke-width="2"/></svg><h4>EASY TO USE</h4><p>Our on-hand "Marketing Minds" are available via phone (Mon-Thurs 7AM-5PM &amp; Fri 7AM-3PM MST)</p></div>
  <div class="why-item" style="left:790px;top:290px"><svg viewBox="0 0 40 40"><path d="M22 3h14v14L17 36 3 22z" fill="none" stroke="#333" stroke-width="2"/><circle cx="29" cy="10" r="2.5" fill="none" stroke="#333" stroke-width="2"/></svg><h4>AUTOMATIC BILLING</h4><p>Our on-hand "Marketing Minds" are available via phone (Mon-Thurs 7AM-5PM &amp; Fri 7AM-3PM MST)</p></div>
</section>

<section class="testimonial" role="img" aria-label="Dimmed photo of hands typing on a laptop behind a customer testimonial">
  <div class="avatar" role="img" aria-label="Customer portrait"></div>
  <p class="quote">"I switched suppliers &amp; now have MsgZeta. Training, support, &amp; functionality are superb.<br>This will be a long term relationship."</p>
  <p class="quote-author">Dana R., UT</p>
  <div class="dots"><i></i><i></i><i></i></div>
</section>

<section class="clients">
  <h2 class="section-title">SATISFIED CLIENTS</h2>
  <div class="client" style="left:132px"><i></i>Brightbite</div>
  <div class="client" style="left:375px">Fernroll</div>
  <div class="client" style="left:614px">Kelvar</div>
  <div class="client" style="left:852px">Fizzora</div>
</section>

<footer class="site-footer">
  <div class="footer-col" style="left:132px"><h4>QUICK LINKS</h4><ul><li>Home</li><li>Pricing</li><li>Benefits</li><li>How it works</li><li>Resellers</li><li>Sign up</li></ul></div>
  <div class="footer-col" style="left:371px"><h4>HOW TO USE</h4><ul><li>How It Works</li><li>Videos</li><li>FAQs</li><li>Support</li></ul></div>
  <div class="footer-col" style="left:587px"><h4>CONTACT US</h4><ul><li>410 N. Cedar Ridge Ave #12</li><li>Mesa Vista, UT 84000</li><li>&nbsp;</li><li>Phone: 1 (800) 555-0142</li><li>Send Us A Message</li></ul></div>
  <div class="footer-brand"><span class="brand-mark"></span><span class="brand-name">MsgZeta</span></div>
</footer>
<div class="footer-bar">
  <p class="copy">© MsgZeta. All rights reserved. &nbsp;Privacy / Terms</p>
  <div class="social"><i></i><i></i><i></i></div>
</div>

</body>
</html>
```